Brantley Advisory Group provides support for renewable energy projects to utilities and suppliers

I need a professional looking business card that is both simple and elegant and unique. My clients are mostly large organizations not individuals. I am a consultant with my own company that is small but would like to give clients the impression I am larger. Smart grid, fiber optics, software, field hardware, distribution automation, substation automation, operations, energy storage/batteries, microgrids, customer service, strategy/roadmaps, conservation, Automated Metering Infrastruture (AMI or smart meters) are all areas of focus.

Target Market(s)

Utilities, suppliers, governmental agencies involved in energy. All types of energy especially natural gas and electrical. Especially renewable energy or green projects.

Contact Information for Business Card

Name - Dorian Kettleby Cell Phone - 425.318.2746 Email - dkettleby@brantleyag-example.com
Company - Brantley Advisory Group (logo) Title - Principal

Font styles to use
Serif
Sans Serif

Colors

Designer to choose colors to be used in the design.

Requirements
Must have
• Simple and professional and powerful.
• Unique/creative design.
Nice to have
• Utilize color scheme to accent logo colors. Maybe some geometric pattern on edge of card with color.
Should not have
• Busy, complicated, traditional

```html
<!DOCTYPE html>
<html lang="en">
<head>
<meta charset="utf-8">
<title>Brantley Advisory Group – Business Card</title>
<link rel="stylesheet" href="https://fonts.googleapis.com/css2?family=Questrial&display=swap">
<style>
  :root {
    --bg: #8a8985;
    --paper: #ffffff;
    --brand-blue: #2a05a8;
    --brand-blue-deep: #22068c;
    --ink: #111111;
    --muted: #333333;
    --band-black: #050505;
  }
  * { box-sizing: border-box; margin: 0; padding: 0; }
  html, body {
    width: 1200px; height: 855px; overflow: hidden;
    background: var(--bg);
    font-family: "Questrial", Arial, sans-serif;
  }
  .canvas {
    position: relative; width: 1200px; height: 855px;
    display: flex; flex-direction: column; align-items: center; justify-content: center; gap: 32px;
  }
  .card {
    position: relative; width: 640px; height: 366px;
    border-radius: 34px; overflow: hidden;
    box-shadow: 0 10px 24px rgba(0,0,0,.25);
  }

  /* Front */
  .card-front { background: var(--paper); }
  .front-brand {
    position: absolute; left: 70px; top: 128px;
    display: flex; align-items: center; gap: 16px;
  }
  .brand-square {
    flex: none; width: 34px; height: 34px; border: 3px solid var(--brand-blue); border-radius: 5px;
  }
  .brand-name {
    font-size: 26px; line-height: 1.1; color: var(--brand-blue); width: 190px;
  }
  .divider {
    position: absolute; left: 338px; top: 92px; width: 2px; height: 90px;
    background: var(--brand-blue);
  }
  .contact { position: absolute; left: 372px; top: 92px; }
  .person-name { font-size: 22px; color: var(--brand-blue); }
  .person-title { font-size: 13px; color: var(--muted); margin-bottom: 22px; }
  .contact-line {
    display: flex; align-items: center; gap: 10px;
    font-family: Arial, sans-serif; font-size: 11px; letter-spacing: .8px; color: var(--ink);
    margin-bottom: 8px; white-space: nowrap;
  }
  .contact-icon { width: 14px; height: 14px; flex: none; }
  .band-blue {
    position: absolute; left: 0; bottom: 0; width: 400px; height: 10px;
    background: var(--brand-blue);
    clip-path: polygon(0 0, 100% 0, 99% 100%, 0 100%);
  }
  .band-black {
    position: absolute; right: 0; bottom: 0; width: 250px; height: 40px;
    background: var(--band-black);
    clip-path: polygon(6% 0, 100% 0, 100% 100%, 0 100%);
    display: flex; align-items: center; justify-content: flex-end; padding-right: 34px;
    color: #fff; font-size: 14px; white-space: nowrap;
  }

  /* Back */
  .card-back { background: var(--brand-blue); }
  .world-map {
    position: absolute; inset: 30px 50px;
    background: radial-gradient(ellipse at center, rgba(20,6,110,.55), rgba(20,6,110,0) 70%);
  }
  .back-brand {
    position: absolute; inset: 0;
    display: flex; align-items: center; justify-content: center; gap: 20px;
  }
  .back-brand .brand-square { border-color: #fff; width: 48px; height: 48px; border-width: 4px; }
  .back-brand .brand-name { color: #fff; font-size: 38px; width: auto; white-space: nowrap; }
</style>
</head>
<body>
<main class="canvas">
  <section class="card card-front">
    <div class="front-brand">
      <span class="brand-square"></span>
      <span class="brand-name">Brantley Advisory Group</span>
    </div>
    <div class="divider"></div>
    <div class="contact">
      <p class="person-name">Dorian Kettleby</p>
      <p class="person-title">Principal</p>
      <p class="contact-line">
        <svg class="contact-icon" viewBox="0 0 14 14"><circle cx="7" cy="7" r="7" fill="#2a05a8"/><path d="M4.5 3.5l1.5 0 .6 1.8-.9.7a5 5 0 0 0 2.3 2.3l.7-.9 1.8.6v1.5c-3.5.3-6.3-2.5-6-6z" fill="#fff"/></svg>
        425.318.2746
      </p>
      <p class="contact-line">
        <svg class="contact-icon" viewBox="0 0 14 14"><circle cx="7" cy="7" r="7" fill="#2a05a8"/><rect x="3.5" y="4.5" width="7" height="5" fill="none" stroke="#fff" stroke-width="1"/><path d="M3.5 4.5l3.5 3 3.5-3" fill="none" stroke="#fff" stroke-width="1"/></svg>
        dkettleby@brantleyag-example.com
      </p>
    </div>
    <div class="band-blue"></div>
    <div class="band-black">Brantley Advisory Group</div>
  </section>

  <section class="card card-back">
    <div class="world-map" role="img" aria-label="Faint world map in deep blue tones behind the brand name"></div>
    <div class="back-brand">
      <span class="brand-square"></span>
      <span class="brand-name">Brantley Advisory Group</span>
    </div>
  </section>
</main>
</body>
</html>
```